RESIDENTIAL CONSTRUCTION

We are a company that specializes in building custom residential homes, the design should also emphasize that quality and service is our priority.

Industry/Entity Type

Construction Company

Contact Information for Business Card

Contact Person: Tobias Lindqvar
Company Address: 463 Westbrook Ave San Jose , Ca 95112
Phone Number : 408-731-2946
Email Address: Oakfieldcrafters731@mailvessel.net

Font styles to use
Sans Serif

Colors
ec1f27

Requirements
Must have
• CSLB # 7362519
Nice to have
• needs to have same color as logo i uploaded, we will be printing these on a clear plastic card.

```html
<!DOCTYPE html>
<html lang="en">
<head>
<meta charset="UTF-8">
<title>Oakfield Crafters – Business Card</title>
<link href="https://fonts.googleapis.com/css2?family=Oswald:wght@500;600&family=Lato:wght@400;700&display=swap" rel="stylesheet">
<style>
  :root {
    --page-bg: #e4e8ec;
    --card-bg: rgba(236, 242, 247, 0.92);
    --card-edge: #c7d0d8;
    --brand-red: #ec1f27;
    --deep-red: #a3212a;
    --ink: #1e1e22;
    --ruler: #2a2a2e;
  }
  * { box-sizing: border-box; margin: 0; padding: 0; }
  html, body { width: 1200px; height: 900px; overflow: hidden; }
  body { background: var(--page-bg); position: relative; font-family: "Lato", sans-serif; }

  .card {
    position: absolute; left: 220px; top: 235px;
    width: 760px; height: 430px;
    background: var(--card-bg);
    border: 1px solid var(--card-edge);
    border-radius: 6px;
    box-shadow: 0 8px 24px rgba(40, 50, 60, 0.12);
  }

  /* ruler frame */
  .ruler { position: absolute; }
  .ruler--top {
    left: 20px; top: 22px; width: 685px; height: 20px;
    border-bottom: 2px solid var(--ruler);
    background:
      repeating-linear-gradient(90deg, var(--ruler) 0 1.5px, transparent 1.5px 55px) bottom / 100% 20px no-repeat,
      repeating-linear-gradient(90deg, var(--ruler) 0 1.5px, transparent 1.5px 11px) bottom / 100% 9px no-repeat;
  }
  .ruler--bottom {
    left: 110px; top: 362px; width: 620px; height: 20px;
    border-top: 2px solid var(--ruler);
    background:
      repeating-linear-gradient(90deg, var(--ruler) 0 1.5px, transparent 1.5px 55px) top / 100% 20px no-repeat,
      repeating-linear-gradient(90deg, var(--ruler) 0 1.5px, transparent 1.5px 11px) top / 100% 9px no-repeat;
  }
  .ruler--left {
    left: 18px; top: 58px; width: 30px; height: 310px;
    border-right: 2px solid var(--ruler);
    background:
      repeating-linear-gradient(180deg, var(--ruler) 0 1.5px, transparent 1.5px 46px) right / 30px 100% no-repeat,
      repeating-linear-gradient(180deg, var(--ruler) 0 1.5px, transparent 1.5px 11.5px) right / 14px 100% no-repeat;
  }
  .ruler--right {
    left: 702px; top: 22px; width: 30px; height: 350px;
    border-left: 3px solid var(--ruler);
    background:
      repeating-linear-gradient(180deg, var(--ruler) 0 2px, transparent 2px 46px) left / 30px 100% no-repeat,
      repeating-linear-gradient(180deg, var(--ruler) 0 2px, transparent 2px 8px) left / 12px 100% no-repeat;
  }

  /* mark area */
  .brand-mark {
    position: absolute; left: 82px; top: 92px; width: 220px; height: 240px;
    display: flex; flex-direction: column; align-items: center; justify-content: center; gap: 18px;
  }
  .brand-mark__square { width: 70px; height: 70px; background: var(--deep-red); }
  .brand-mark__name {
    font-family: "Oswald", sans-serif; font-weight: 600;
    font-size: 30px; line-height: 1.1; text-align: center;
    color: var(--deep-red); text-transform: uppercase;
  }

  /* details */
  .details { position: absolute; left: 358px; top: 80px; width: 340px; color: var(--ink); }
  .company-name {
    font-family: "Oswald", sans-serif; font-weight: 600;
    font-size: 34px; line-height: 1; color: var(--deep-red);
    text-transform: uppercase; letter-spacing: 0.5px;
  }
  .license { margin-top: 26px; font-size: 17px; letter-spacing: 0.5px; }
  .person {
    margin-top: 28px;
    font-family: "Oswald", sans-serif; font-weight: 500;
    font-size: 31px; line-height: 1; color: #7a1c25;
    text-transform: uppercase; letter-spacing: 0.5px;
  }
  .address { margin-top: 12px; font-size: 17px; line-height: 1.3; }
  .contact-list { list-style: none; margin-top: 12px; }
  .contact-list li { display: flex; align-items: center; gap: 12px; font-size: 17px; line-height: 1.6; }
  .contact-list svg { width: 13px; height: 13px; flex: none; }
</style>
</head>
<body>
  <section class="card" aria-label="Oakfield Crafters business card">
    <div class="ruler ruler--top"></div>
    <div class="ruler ruler--right"></div>
    <div class="ruler ruler--left"></div>
    <div class="ruler ruler--bottom"></div>

    <div class="brand-mark">
      <div class="brand-mark__square"></div>
      <div class="brand-mark__name">Oakfield<br>Crafters</div>
    </div>

    <div class="details">
      <h1 class="company-name">Oakfield Crafters</h1>
      <p class="license">CSLB # 7362519</p>
      <h2 class="person">Tobias Lindqvar</h2>
      <p class="address">463 Westbrook Ave San Jose<br>Ca 95112</p>
      <ul class="contact-list">
        <li>
          <svg viewBox="0 0 12 12" aria-hidden="true"><rect x="3" y="0.5" width="6" height="11" rx="1.2" fill="none" stroke="#a3212a" stroke-width="1.5"/><circle cx="6" cy="9.5" r="0.8" fill="#a3212a"/></svg>
          <span>408-731-2946</span>
        </li>
        <li>
          <svg viewBox="0 0 12 12" aria-hidden="true"><rect x="0.5" y="2" width="11" height="8" fill="#a3212a"/><path d="M0.5 2.5 L6 6.5 L11.5 2.5" fill="none" stroke="#ffffff" stroke-width="1"/></svg>
          <span>Oakfieldcrafters731@mailvessel.net</span>
        </li>
      </ul>
    </div>
  </section>
</body>
</html>
```